MAPLEHAVEN

We just changed our name from Quintells to Mapplehaven so we need a new website. have been in the catering &special events business for 36 years . We are an in house caterer with homemade food and best around our name has always hurt us so we changed it and want a new web site to go with it. The current website Quintells banquet center .com can be viewed but, is horrible. I have been to many website companies in the past years and have never had a profesinal website. What brides want to see on the web are pictures and I feel they do not necessarily have to be from this facility they can be stock photos that resemble this place.

Target Market(s)

weddings partys

Industry/Entity Type

Business

Number of Pages Required

5+ page

Requirements
Must have
• pictures
Nice to have
• we have done functions for the king of Jordan on his plane and other famous people including celebrities and stars. This was when we were doing airline catering years ago, but, does not matter if plane or our facility they do not need to know that. Their were many people who have come to us from all over the world for private functions. Consider the possibilities memorable Weddings, exciting anniversaries and birthday parties .

```html
<!DOCTYPE html>
<html lang="en">
<head>
<meta charset="utf-8">
<title>Maplehaven – Banquet & Conference Center</title>
<link href="https://fonts.googleapis.com/css2?family=Roboto:ital,wght@0,300;0,400;0,500;0,700;1,400&display=swap" rel="stylesheet">
<style>
:root{
  --red:#d63a45;
  --ink:#2b2b2b;
  --text:#555;
  --muted:#888;
  --band:#dedbd6;
  --line:#cfcfcf;
  --dark:#1f1f1f;
  --footer:#262626;
  --plum:#5b2a4c;
  --white:#fff;
}
*{box-sizing:border-box;margin:0;padding:0}
html,body{width:1200px;height:4534px;overflow:hidden}
body{font-family:'Roboto',sans-serif;color:var(--text);background:var(--white);position:relative}
section,header,footer{position:relative;width:1200px}
.accent{color:var(--red);font-weight:700}

/* header */
.site-header{height:66px;display:flex;align-items:center;padding:0 73px}
.brand{font-size:27px;font-weight:500;color:var(--ink);letter-spacing:.5px}
.main-nav{display:flex;gap:30px;margin-left:178px;font-size:14px;font-weight:500;color:var(--ink)}
.header-phone{margin-left:auto;display:flex;align-items:center;gap:8px;font-size:15px;font-weight:500;color:var(--ink)}

/* hero */
.hero{height:584px;background:linear-gradient(180deg,#3a3a48 0%,#5a4a44 30%,#8a5a32 48%,#3b2d2a 70%,#1d1b22 100%)}
.hero-badge{position:absolute;left:393px;top:342px;width:410px;height:120px;border-radius:60px;background:var(--plum);border:3px solid rgba(255,255,255,.55);display:flex;align-items:center;justify-content:center;color:#fff;font-size:46px;font-weight:300}
.hero-badge b{font-weight:700;margin-left:12px}

/* section headings */
.lined-title{display:flex;align-items:center;gap:20px;margin:0 73px;font-size:30px;font-weight:400;color:var(--ink);white-space:nowrap}
.lined-title::before,.lined-title::after{content:"";flex:1;height:1px;background:var(--line)}

/* welcome */
.welcome{height:350px;padding-top:68px}
.welcome-copy{margin:30px auto 0;width:1050px;text-align:center;font-size:14px;line-height:26px;color:var(--muted)}
.welcome-copy p+p{margin-top:20px}

/* slanted bands */
.band{position:absolute;left:0;width:1200px;background:var(--band);clip-path:polygon(0 70px,100% 0,100% calc(100% - 70px),0 100%)}
.tab{position:absolute;left:73px;height:84px;width:650px;background:var(--red);clip-path:polygon(0 0,100% 40%,100% 100%,0 100%);color:#fff;font-size:30px;font-weight:300;display:flex;align-items:center;padding:20px 0 0 28px;z-index:2}
.tab b{font-weight:700;margin-left:8px}

/* services */
.services{height:720px}
.services .band{top:43px;height:650px}
.services .tab{top:19px}
.service-grid{position:absolute;left:73px;top:152px;width:1052px;display:grid;grid-template-columns:repeat(4,242px);column-gap:28px;row-gap:19px}
.service-photo{height:178px}
.service-name{margin-top:14px;font-size:18px;color:var(--ink)}

/* featured */
.featured{height:480px}
.featured-col{position:absolute;top:97px;width:330px}
.featured-title{font-size:20px;font-weight:400;color:var(--ink);margin-bottom:22px}
.featured-text{font-size:13.5px;line-height:24px;color:var(--text)}
.read-more{display:flex;align-items:center;gap:8px;margin-top:24px;font-size:13px;font-weight:500;color:var(--ink)}

/* events */
.events{height:660px}
.events .band{top:52px;height:559px}
.events .tab{top:16px}
.event-grid{position:absolute;left:73px;top:158px;width:1052px;display:grid;grid-template-columns:repeat(4,242px);column-gap:28px}
.event-card{background:#fff;height:393px;box-shadow:0 1px 3px rgba(0,0,0,.08)}
.event-photo{height:175px;position:relative}
.event-date{position:absolute;left:12px;bottom:0;width:72px;height:42px;background:#fff;display:flex;align-items:center;justify-content:center;gap:6px;color:var(--ink)}
.event-date b{font-size:22px}
.event-date span{font-size:9px;line-height:10px;color:var(--muted)}
.event-body{padding:18px 16px}
.event-title{font-size:15px;font-weight:700;line-height:21px;color:var(--ink)}
.event-text{margin-top:14px;font-size:13px;line-height:19px;color:var(--muted)}
.event-body .read-more{margin-top:12px}

/* gallery */
.gallery{height:852px;padding-top:83px}
.gallery-grid{position:absolute;left:73px;top:157px;width:1052px;height:460px}
.gallery-grid div{position:absolute;width:257px}
.gallery-button{position:absolute;left:475px;top:728px;width:250px;height:46px;border:1px solid #bbb;display:flex;align-items:center;justify-content:center;font-size:13px;color:var(--ink)}

/* testimonials */
.testimonials{height:405px;background:linear-gradient(180deg,#121417 0%,#24302c 55%,#181a1e 100%);color:#fff;text-align:center}
.testimonials .lined-title{position:absolute;top:70px;left:330px;right:330px;margin:0;color:#fff;font-size:28px}
.testimonials .lined-title::before,.testimonials .lined-title::after{background:rgba(255,255,255,.35)}
.testimonials .accent{color:#fff}
.quote{position:absolute;left:200px;width:800px;top:148px;font-size:16px;font-style:italic;line-height:27px;color:#eee}
.author{position:absolute;left:520px;top:240px;display:flex;align-items:center;gap:12px;text-align:left;font-size:13px;line-height:17px}
.avatar{width:56px;height:56px;border-radius:50%;background:linear-gradient(#e7c0a0,#c79775);border:3px solid #fff}
.dots{position:absolute;left:0;right:0;top:340px;display:flex;justify-content:center;gap:7px}
.dots i{width:10px;height:10px;border-radius:50%;background:#fff}
.dots i:first-child{background:var(--red)}

/* footer */
.site-footer{height:417px;background:var(--footer);color:#ccc;font-size:13px}
.footer-col{position:absolute;top:79px}
.footer-col h4{font-size:13px;font-weight:700;color:#fff;margin-bottom:16px}
.footer-links li{list-style:none;line-height:20px}
.footer-map{margin-top:20px;width:232px;height:136px;background:linear-gradient(135deg,#e9e5dc,#d5dccf)}
.social{display:flex;gap:14px;margin-bottom:30px}
.social i{width:22px;height:22px;background:#cfcfcf;display:block}
.contact-label{font-size:15px;color:#fff;margin-top:12px}
.contact-value{font-size:22px;font-weight:500;color:#fff;margin-top:4px}
.contact-value.small{font-size:14px;font-weight:400}
.copyright{position:absolute;left:73px;top:373px;font-size:12px;color:#ccc}
.help-form{position:absolute;left:792px;top:-8px;width:333px;height:396px;background:var(--red);padding:22px 18px}
.help-form h3{font-size:28px;font-weight:300;color:#fff;text-align:center;margin-bottom:16px}
.help-form h3 b{font-weight:700}
.field{height:34px;background:#fff;margin-bottom:11px;padding:0 12px;display:flex;align-items:center;font-size:12px;color:#999}
.field.message{height:70px;align-items:flex-start;padding-top:10px}
.submit{height:44px;background:var(--dark);color:#fff;font-size:14px;font-weight:700;display:flex;align-items:center;justify-content:center;margin-top:6px}
</style>
</head>
<body>

<header class="site-header">
  <div class="brand">MAPLEHAVEN</div>
  <nav class="main-nav"><span>HOME</span><span>ABOUT US</span><span>SERVICES</span><span>GALLERY</span><span>CONTACT US</span></nav>
  <div class="header-phone">
    <svg width="16" height="16" viewBox="0 0 24 24"><path fill="#2b2b2b" d="M6.6 10.8a15.1 15.1 0 0 0 6.6 6.6l2.2-2.2c.3-.3.7-.4 1-.2 1.1.4 2.3.6 3.6.6.6 0 1 .4 1 1V20c0 .6-.4 1-1 1A17 17 0 0 1 3 4c0-.6.4-1 1-1h3.5c.6 0 1 .4 1 1 0 1.3.2 2.5.6 3.6.1.3 0 .7-.2 1z"/></svg>
    (555) 014-2379
  </div>
</header>

<section class="hero" role="img" aria-label="Evening photo of a lit outdoor reception tent beside a reflecting pool">
  <div class="hero-badge">Beautiful<b>Venues.</b></div>
</section>

<section class="welcome">
  <h2 class="lined-title"><span>Welcome to <span class="accent">Mapplehaven</span></span></h2>
  <div class="welcome-copy">
    <p>Imagine your wedding in a picturesque Alder Valley rural setting with an elegant grand ballroom to delight your guests along with a fabulous glass enclosed atrium. Mapplehaven beautiful setting includes a huge outdoor reception area and terrace with a magnificent garden.</p>
    <p>Mapplehaven features mouth-watering homemade entrees and offers award winning fruit and cheese displays. All this includes the most special attention to answer your every want and desire for a fantastic wedding reception. Mapplehaven also features custom catering for all types of social and professional events. And all at a surprisingly reasonable price to you...</p>
  </div>
</section>

<section class="services">
  <div class="band"></div>
  <div class="tab">Our<b>Services</b></div>
  <div class="service-grid">
    <div><div class="service-photo" role="img" aria-label="Bride in white gown" style="background:linear-gradient(135deg,#e8e2d8,#b8a894)"></div><div class="service-name">Weddings</div></div>
    <div><div class="service-photo" role="img" aria-label="Banquet hall with set tables" style="background:linear-gradient(135deg,#8a6a3e,#3e2a18)"></div><div class="service-name">Banquets</div></div>
    <div><div class="service-photo" role="img" aria-label="Guests at a fund raiser dinner" style="background:linear-gradient(135deg,#c89a6a,#7a5a8a)"></div><div class="service-name">Fund Raisers</div></div>
    <div><div class="service-photo" role="img" aria-label="Guests celebrating a retirement party" style="background:linear-gradient(135deg,#b8a88a,#6a7a8a)"></div><div class="service-name">Retirement Parties</div></div>
    <div><div class="service-photo" role="img" aria-label="Birthday party with cake and candles" style="background:linear-gradient(135deg,#3a2a6a,#c84a8a)"></div><div class="service-name">Birthdays</div></div>
    <div><div class="service-photo" role="img" aria-label="Bar with bottles and glasses" style="background:linear-gradient(135deg,#4a3a2a,#1a1410)"></div><div class="service-name">Bar</div></div>
    <div><div class="service-photo" role="img" aria-label="Bat mitzvah party with lit stage" style="background:linear-gradient(135deg,#2a2a3a,#7a7a9a)"></div><div class="service-name">Bat Mitzvahs</div></div>
    <div><div class="service-photo" role="img" aria-label="Decorated hall for any occasion" style="background:linear-gradient(135deg,#6a5a5a,#2a2222)"></div><div class="service-name">All Occasions</div></div>
  </div>
</section>

<section class="featured">
  <article class="featured-col" style="left:73px">
    <h3 class="featured-title">Featured <span class="accent">Professional</span></h3>
    <p class="featured-text">Lorem ipsum dolor sit amet, consectetur adipiscing elit, sed do eiusmod tempor incididunt ut labore et dolore magna aliqua. Ut enim ad minim veniam, quis nostrud exercitation ullamco laboris nisi ut aliquip ex ea commodo consequat. Duis aute irure dolor in reprehenderit in voluptate velit esse cillum dolore eu fugiat nulla pariatur. Excepteur sint occaecat cupidatat non proident, sunt in culpa qui officia deserunt mollit anim id est laborum.</p>
    <div class="read-more">Read More <svg width="16" height="10" viewBox="0 0 16 10"><path d="M0 5h14M10 1l4 4-4 4" stroke="#2b2b2b" fill="none" stroke-width="1.4"/></svg></div>
  </article>
  <article class="featured-col" style="left:432px">
    <h3 class="featured-title">We <span class="accent">Are Number One</span></h3>
    <p class="featured-text">Lorem ipsum dolor sit amet, consectetur adipiscing elit, sed do eiusmod tempor incididunt ut labore et dolore magna aliqua. Ut enim ad minim veniam, quis nostrud exercitation ullamco laboris nisi ut aliquip ex ea commodo consequat. Duis aute irure dolor in reprehenderit in voluptate velit esse cillum dolore eu fugiat nulla pariatur. Excepteur sint occaecat cupidatat non proident, sunt in culpa qui officia deserunt mollit anim id est laborum.</p>
    <div class="read-more">Read More <svg width="16" height="10" viewBox="0 0 16 10"><path d="M0 5h14M10 1l4 4-4 4" stroke="#2b2b2b" fill="none" stroke-width="1.4"/></svg></div>
  </article>
  <article class="featured-col" style="left:792px">
    <h3 class="featured-title">Featured <span class="accent">Venue</span></h3>
    <p class="featured-text">Lorem ipsum dolor sit amet, consectetur adipiscing elit, sed do eiusmod tempor incididunt ut labore et dolore magna aliqua. Ut enim ad minim veniam, quis nostrud exercitation ullamco laboris nisi ut aliquip ex ea commodo consequat. Duis aute irure dolor in reprehenderit in voluptate velit esse cillum dolore eu fugiat nulla pariatur. Excepteur sint occaecat cupidatat non proident, sunt in culpa qui officia deserunt mollit anim id est laborum.</p>
    <div class="read-more">Read More <svg width="16" height="10" viewBox="0 0 16 10"><path d="M0 5h14M10 1l4 4-4 4" stroke="#2b2b2b" fill="none" stroke-width="1.4"/></svg></div>
  </article>
</section>

<section class="events">
  <div class="band"></div>
  <div class="tab">Feature<b>Event</b></div>
  <div class="event-grid">
    <article class="event-card">
      <div class="event-photo" role="img" aria-label="Grand ballroom with chandeliers" style="background:linear-gradient(135deg,#c8b078,#5a4a2a)"><div class="event-date"><b>19</b><span>FEB<br>2017</span></div></div>
      <div class="event-body"><div class="event-title">Lorem ipsum dolor sit amet, consectetur adipiscing elit,</div><p class="event-text">Sed ut perspiciatis unde omnis iste natus error sit voluptatem accusantium doloremque laudantium, totam.</p><div class="read-more">Read More <svg width="16" height="10" viewBox="0 0 16 10"><path d="M0 5h14M10 1l4 4-4 4" stroke="#2b2b2b" fill="none" stroke-width="1.4"/></svg></div></div>
    </article>
    <article class="event-card">
      <div class="event-photo" role="img" aria-label="Bride posing in a garden" style="background:linear-gradient(135deg,#3a5a3a,#1a2a1a)"><div class="event-date"><b>19</b><span>FEB<br>2017</span></div></div>
      <div class="event-body"><div class="event-title">Lorem ipsum dolor sit amet, consectetur adipiscing elit,</div><p class="event-text">Sed ut perspiciatis unde omnis iste natus error sit voluptatem accusantium doloremque laudantium, totam.</p><div class="read-more">Read More <svg width="16" height="10" viewBox="0 0 16 10"><path d="M0 5h14M10 1l4 4-4 4" stroke="#2b2b2b" fill="none" stroke-width="1.4"/></svg></div></div>
    </article>
    <article class="event-card">
      <div class="event-photo" role="img" aria-label="Table set with floral arrangements" style="background:linear-gradient(135deg,#6a8a4a,#c86a4a)"><div class="event-date"><b>19</b><span>FEB<br>2017</span></div></div>
      <div class="event-body"><div class="event-title">Lorem ipsum dolor sit amet, consectetur adipiscing elit,</div><p class="event-text">Sed ut perspiciatis unde omnis iste natus error sit voluptatem accusantium doloremque laudantium, totam.</p><div class="read-more">Read More <svg width="16" height="10" viewBox="0 0 16 10"><path d="M0 5h14M10 1l4 4-4 4" stroke="#2b2b2b" fill="none" stroke-width="1.4"/></svg></div></div>
    </article>
    <article class="event-card">
      <div class="event-photo" role="img" aria-label="Reception hall with round tables" style="background:linear-gradient(135deg,#b89a6a,#4a3a2a)"><div class="event-date"><b>19</b><span>FEB<br>2017</span></div></div>
      <div class="event-body"><div class="event-title">Lorem ipsum dolor sit amet, consectetur adipiscing elit,</div><p class="event-text">Sed ut perspiciatis unde omnis iste natus error sit voluptatem accusantium doloremque laudantium, totam.</p><div class="read-more">Read More <svg width="16" height="10" viewBox="0 0 16 10"><path d="M0 5h14M10 1l4 4-4 4" stroke="#2b2b2b" fill="none" stroke-width="1.4"/></svg></div></div>
    </article>
  </div>
</section>

<section class="gallery">
  <h2 class="lined-title"><span>Photo <span class="accent">Gallery</span></span></h2>
  <div class="gallery-grid">
    <div role="img" aria-label="Garden statue beside a stone wall" style="left:0;top:0;height:356px;background:linear-gradient(135deg,#c8c0b0,#5a5448)"></div>
    <div role="img" aria-label="Ballroom with chandeliers" style="left:0;top:362px;height:98px;background:linear-gradient(135deg,#4a3a2a,#1a1410)"></div>
    <div role="img" aria-label="Plated dinner under warm light" style="left:265px;top:0;height:172px;background:linear-gradient(135deg,#5a4a3a,#c8a070)"></div>
    <div role="img" aria-label="Garden terrace with gazebo" style="left:265px;top:178px;height:282px;background:linear-gradient(180deg,#d8e0e8,#6a7a4a 55%,#8a7a6a)"></div>
    <div role="img" aria-label="Snowy grounds at night" style="left:530px;top:0;height:172px;background:linear-gradient(135deg,#2a3a5a,#c8d0e0)"></div>
    <div role="img" aria-label="Hall lit with string lights" style="left:530px;top:178px;height:172px;background:linear-gradient(135deg,#1a1410,#8a5a2a 50%,#2a1e14)"></div>
    <div role="img" aria-label="Dance floor under purple party lights" style="left:530px;top:356px;height:104px;background:linear-gradient(135deg,#3a1a6a,#b84ac8)"></div>
    <div role="img" aria-label="Buffet platters of food" style="left:795px;top:0;height:172px;background:linear-gradient(135deg,#c86a3a,#f0e8d8)"></div>
    <div role="img" aria-label="Bride standing in a doorway" style="left:795px;top:178px;height:282px;background:linear-gradient(135deg,#1a1a1a,#e8e8e8 50%,#2a3a2a)"></div>
  </div>
  <div class="gallery-button">View All Photos in The Gallery</div>
</section>

<section class="testimonials" role="group" aria-label="Testimonials">
  <h2 class="lined-title"><span>What <span class="accent">People Are Saying</span></span></h2>
  <p class="quote">"Lorem ipsum dolor sit amet, consectetur adipiscing elit, sed do eiusmod tempor incididunt ut labore et dolore magna aliqua. Ut enim ad minim veniam, quis nostrud exercitation ullamco laboris nisi ut aliquip ex ea commodo consequat. Duis aute irure dolor in reprehenderit in voluptate velit esse cillum dolore eu fugiat nulla pariatur."</p>
  <div class="author"><div class="avatar" role="img" aria-label="Portrait of the reviewer"></div><div>Dana<br>Whitfield</div></div>
  <div class="dots"><i></i><i></i><i></i><i></i><i></i></div>
</section>

<footer class="site-footer">
  <div class="footer-col" style="left:73px">
    <h4>Quick Links</h4>
    <ul class="footer-links"><li>Home</li><li>About Us</li><li>Services</li><li>Gallery</li><li>Contact Us</li></ul>
  </div>
  <div class="footer-col" style="left:208px">
    <h4>Contact Us</h4>
    <p style="line-height:20px">Mapplehaven Banquet &amp; Conf Center<br>418 Orchard Rd, Millbrook,<br>NJ 08000</p>
    <div class="footer-map" role="img" aria-label="Street map showing the location of Mapplehaven Banquet &amp; Conf Center"></div>
  </div>
  <div class="footer-col" style="left:496px">
    <h4>Get Connect with us</h4>
    <div class="social"><i></i><i></i><i></i><i></i><i></i></div>
    <div class="contact-label">Phone</div>
    <div class="contact-value">(555) 014-2379</div>
    <div class="contact-label">Fax</div>
    <div class="contact-value">(555) 014-2160</div>
    <div class="contact-label">Email</div>
    <div class="contact-value small">events@maplehaven.net</div>
  </div>
  <form class="help-form">
    <h3>How <b>Can We Help?</b></h3>
    <div class="field">First Name</div>
    <div class="field">Last Name</div>
    <div class="field">E-Mail Address</div>
    <div class="field">Phone Number</div>
    <div class="field message">Your Message</div>
    <div class="submit">SUBMIT</div>
  </form>
  <div class="copyright">Copyright © 2017 Mapplehaven.</div>
</footer>

</body>
</html>
```